Business Card for Musician

The company is called Velkor Music Entertainment and i am the director (Miles Tenney) . I would like a logo made along with a list of services i provide :

Rock Pop and Jazz Covers music for Weddings , Birthdays , Pubs, Bars and Restaurants

I provide Solo/Duo and Bands for these functions.

Another aspect is i teach guitar and do music workshops and compose music for television.

I want to go for something different than a photo of a guitar or singer..i like the idea of soundwaves and an ear. or ripples of sound like a music note (as a drop of water) and the sound rippling out..another idea is something with lighting (music lights) with different colours lighting up the name Velkor..however im open to any ideas. Thanks

Target Market(s)

General Public, Music Agents, Venue Owners. English Speaking..adults from 25-50

Industry/Entity Type

Business

Font styles to use
Sans Serif

Colors

Designer to choose colors to be used in the design.

Requirements
Must have
• All the points about what i do...
Nice to have
• Logo could emphasize the VEL in Velkor...
Should not have
• Not too busy please...Simple but gets the message across. NOthing obvious like a photo of a musician playing.

```html
<!DOCTYPE html>
<html lang="en">
<head>
<meta charset="utf-8">
<title>Velkor Music Entertainment – Business Card</title>
<link href="https://fonts.googleapis.com/css2?family=Arimo:wght@700&display=swap" rel="stylesheet">
<style>
  :root {
    --backdrop: #d9dadc;
    --card-black: #070707;
    --ink-white: #ffffff;
  }
  * { margin: 0; padding: 0; box-sizing: border-box; }
  html, body {
    width: 1200px;
    height: 1000px;
    overflow: hidden;
    background: var(--backdrop);
    font-family: "Arimo", Arial, sans-serif;
  }
  .canvas {
    position: relative;
    width: 1200px;
    height: 1000px;
  }
  .business-card {
    position: absolute;
    left: 246px;
    top: 258px;
    width: 706px;
    height: 408px;
    background: var(--card-black);
    border-radius: 14px;
    overflow: hidden;
    color: var(--ink-white);
    font-weight: 700;
  }
  .company-name {
    position: absolute;
    left: 36px;
    top: 30px;
    font-size: 19px;
    letter-spacing: 0.1px;
  }
  .brand-wordmark {
    position: absolute;
    left: 26px;
    top: 150px;
    font-size: 108px;
    line-height: 1;
    letter-spacing: -2px;
  }
  .service-block {
    position: absolute;
    font-size: 14.5px;
    line-height: 20px;
    white-space: nowrap;
    transform-origin: left top;
  }
  .services-styles {
    left: 428px;
    top: 82px;
    transform: rotate(-15deg);
  }
  .services-acts {
    left: 435px;
    top: 178px;
  }
  .services-teaching {
    left: 400px;
    top: 236px;
    transform: rotate(14deg);
  }
</style>
</head>
<body>
  <div class="canvas">
    <section class="business-card">
      <h1 class="company-name">Velkor Music Entertainment</h1>
      <div class="brand-wordmark">Velkor</div>

      <p class="service-block services-styles">
        Rock, Pop and Jazz covers,<br>
        music for Weddings, Birthdays,<br>
        Pubs, Bars and Restaurants.
      </p>

      <p class="service-block services-acts">
        I provide Solo/Duo and Bands<br>
        for these functions.
      </p>

      <p class="service-block services-teaching">
        Another aspect is I teach guitar and<br>
        do music workshops and compose<br>
        music for television.
      </p>
    </section>
  </div>
</body>
</html>
```